QOR Exterior Coatings

double sided. the front i want the name of the business each word on a new line with the QOR being bigger. id like teal, black and white colors. the back i want my contact info. Flat, no gloss. Something professional and I want to feel the letters bump put of the card. if possible maybe a paint sprayer in corner. not a car paint spray. (no tank on top of gun)
no vehicle paint sprayers. that means no tank on top of the gun. doesn't have to have a sprayer. black/dark background on the front. white back ground on back with info

```html
<!DOCTYPE html>
<html lang="en">
<head>
<meta charset="utf-8">
<title>QOR Exterior Coatings – Business Card</title>
<link rel="stylesheet" href="https://fonts.googleapis.com/css2?family=Montserrat:wght@800&family=Open+Sans:wght@400;700&display=swap">
<style>
  :root {
    --stage: #2b2b2c;
    --card-dark: #050505;
    --card-light: #ffffff;
    --ink: #0d0d0d;
    --teal: #1a9ea4;
    --white: #ffffff;
    --spray-light: #d9d9d9;
    --spray-dark: #3a3a3a;
  }
  * { margin: 0; padding: 0; box-sizing: border-box; }
  html, body {
    width: 1200px; height: 900px; overflow: hidden;
    background: var(--stage);
  }
  .stage { position: relative; width: 1200px; height: 900px; }
  .card {
    position: absolute; left: 250px; width: 700px; height: 400px;
    box-shadow: 0 10px 30px rgba(0,0,0,.45);
  }
  .card--front { top: 40px; background: var(--card-dark); }
  .card--back { top: 465px; background: var(--card-light); }

  .brand-name {
    position: absolute;
    font-family: "Montserrat", sans-serif; font-weight: 800;
    line-height: 1; letter-spacing: 2px;
  }
  .brand-tagline {
    position: absolute;
    font-family: "Open Sans", sans-serif; font-weight: 400;
    color: var(--teal); letter-spacing: 2px; text-transform: uppercase;
    white-space: nowrap;
  }

  .card--front .brand-name { left: 235px; top: 128px; font-size: 100px; color: var(--white); }
  .card--front .brand-tagline { left: 237px; top: 242px; font-size: 21px; }
  .spray-art {
    position: absolute; left: 540px; top: 50px; width: 130px; height: 230px;
    background: linear-gradient(160deg, var(--spray-light) 0%, var(--spray-dark) 100%);
    opacity: .35; border-radius: 6px;
  }

  .card--back .brand-name { left: 0; width: 700px; text-align: center; top: 40px; font-size: 128px; color: var(--ink); }
  .card--back .brand-tagline { left: 0; width: 700px; text-align: center; top: 176px; font-size: 30px; }

  .holder-name {
    position: absolute; left: 40px; width: 290px; text-align: right; top: 258px;
    font-family: "Open Sans", sans-serif; font-weight: 700;
    font-size: 30px; color: var(--teal); text-transform: uppercase; white-space: nowrap;
  }
  .divider {
    position: absolute; left: 350px; top: 250px; width: 2px; height: 85px;
    background: var(--ink);
  }
  .contact-list {
    position: absolute; left: 372px; top: 246px; list-style: none;
    font-family: "Open Sans", sans-serif; font-size: 22px; color: var(--ink);
  }
  .contact-list li { display: flex; align-items: center; gap: 12px; height: 31px; white-space: nowrap; }
  .contact-list svg { width: 20px; height: 20px; fill: var(--teal); flex: none; }
  .address {
    position: absolute; left: 0; width: 700px; text-align: center; top: 352px;
    font-family: "Open Sans", sans-serif; font-size: 22px; color: var(--ink);
  }
</style>
</head>
<body>
<main class="stage">

  <section class="card card--front" aria-label="Card front">
    <div class="brand-name">QOR</div>
    <div class="brand-tagline">Exterior Coatings</div>
    <div class="spray-art" role="img" aria-label="Line drawing of a paint spray gun with spray mist"></div>
  </section>

  <section class="card card--back" aria-label="Card back">
    <div class="brand-name">QOR</div>
    <div class="brand-tagline">Exterior Coatings</div>
    <div class="holder-name">Daniel Price</div>
    <div class="divider"></div>
    <ul class="contact-list">
      <li>
        <svg viewBox="0 0 24 24" aria-hidden="true"><path d="M6.6 10.8a15.1 15.1 0 0 0 6.6 6.6l2.2-2.2a1 1 0 0 1 1-.25 11.4 11.4 0 0 0 3.6.57 1 1 0 0 1 1 1V20a1 1 0 0 1-1 1A17 17 0 0 1 3 4a1 1 0 0 1 1-1h3.5a1 1 0 0 1 1 1c0 1.250.2 2.450.57 3.57a1 1 0 0 1-.25 1z"/></svg>
        555-014-2100
      </li>
      <li>
        <svg viewBox="0 0 24 24" aria-hidden="true"><path d="M2 5h20v14H2z M2 5l10 8 10-8" fill="none" stroke="#1a9ea4" stroke-width="2"/></svg>
        hello@qorcoatings.com
      </li>
      <li>
        <svg viewBox="0 0 24 24" aria-hidden="true"><circle cx="12" cy="12" r="9" fill="none" stroke="#1a9ea4" stroke-width="2"/><path d="M3 12h18M12 3c3 3 3 15 0 18M12 3c-3 3-3 15 0 18" fill="none" stroke="#1a9ea4" stroke-width="1.6"/></svg>
        www.qorcoatings.com
      </li>
    </ul>
    <div class="address">Your address, city, state, ZIP 0000</div>
  </section>

</main>
</body>
</html>
```